Corporate Template

Looking for a set of corporate slides to be made which contain multiple different slides and orientations. Looking for at least 8 to 10 different master pages plus a Coversheet and closeout page. Incorporating a color palate similar to our logo coloring is preferred.

I have attached a logo.

```html
<!DOCTYPE html>
<html lang="en">
<head>
<meta charset="utf-8">
<title>Agenda Slide</title>
<link href="https://fonts.googleapis.com/css2?family=Roboto:wght@400;500;700&display=swap" rel="stylesheet">
<style>
  :root {
    --brand-blue: #0a6fba;
    --title-blue: #1a73bf;
    --body-grey: #808080;
    --white: #ffffff;
    --ink: #111111;
    --slice-light-grey: #bfbfbf;
    --slice-grey: #7f7f7f;
    --slice-dark-grey: #595959;
    --slice-deep-blue: #0070c0;
    --slice-mid-blue: #1592e6;
    --slice-pale-blue: #9dd5fc;
  }
  * { margin: 0; padding: 0; box-sizing: border-box; }
  html, body { width: 1200px; height: 900px; overflow: hidden; background: var(--white); }
  body { font-family: "Roboto", Arial, sans-serif; position: relative; }

  .header-band {
    position: absolute; left: 0; top: 0; width: 1200px; height: 102px;
    background: var(--brand-blue);
  }
  .slide-title {
    position: absolute; left: 28px; top: 24px;
    color: var(--white); font-size: 37px; font-weight: 700; line-height: 46px;
  }
  .brand {
    position: absolute; right: 24px; top: 31px;
    display: flex; align-items: center; gap: 12px;
  }
  .brand-dot { width: 22px; height: 22px; border-radius: 50%; background: var(--white); }
  .brand-name {
    color: var(--white); font-size: 30px; font-weight: 400; line-height: 40px;
  }

  .section-title {
    position: absolute; left: 72px; top: 234px;
    color: var(--title-blue); font-size: 30px; font-weight: 700; line-height: 36px;
  }
  .body-copy {
    position: absolute; left: 75px; top: 298px; width: 480px;
    color: var(--body-grey); font-size: 19.5px; line-height: 30px;
  }
  .body-copy p + p { margin-top: 30px; }
  .body-copy .line { display: block; white-space: nowrap; }

  .pie-chart { position: absolute; left: 0; top: 0; width: 1200px; height: 900px; }
  .pie-chart path { stroke: var(--white); stroke-width: 1.5; }
  .slice-label { font-family: "Roboto", Arial, sans-serif; font-size: 16.5px; font-weight: 500; text-anchor: middle; }
  .label-light { fill: var(--white); }
  .label-dark { fill: var(--ink); }

  .footer-band {
    position: absolute; left: 0; top: 860px; width: 1200px; height: 40px;
    background: var(--brand-blue);
  }
  .copyright {
    position: absolute; right: 10px; top: 10px;
    color: var(--white); font-size: 16px; line-height: 20px;
  }
</style>
</head>
<body>
  <header class="header-band">
    <h1 class="slide-title">Agenda Slide</h1>
    <div class="brand">
      <span class="brand-dot"></span>
      <span class="brand-name">Harlow Partners</span>
    </div>
  </header>

  <h2 class="section-title">Graph Slide</h2>
  <div class="body-copy">
    <p>
      <span class="line">Lorem ipsum dolor sit ipsum Lorem ipsum dolor sit</span>
      <span class="line">ipsum Lorem ipsum Lorem ipsum Lorem ipsum</span>
      <span class="line">dolor sit ipsum Lorem ipsum dolor sit ipsum Lorem</span>
      <span class="line">ipsum Lorem ipsum</span>
    </p>
    <p>
      <span class="line">Lorem ipsum dolor sit ipsum Lorem ipsum dolor sit</span>
      <span class="line">ipsum Lorem ipsum Lorem ipsum Lorem ipsum</span>
      <span class="line">dolor sit ipsum Lorem ipsum dolor sit ipsum Lorem</span>
      <span class="line">ipsum Lorem ipsum</span>
    </p>
    <p>
      <span class="line">Lorem ipsum dolor sit ipsum Lorem ipsum dolor sit</span>
      <span class="line">ipsum Lorem ipsum Lorem ipsum Lorem ipsum</span>
      <span class="line">dolor sit ipsum Lorem ipsum dolor sit ipsum Lorem</span>
      <span class="line">ipsum Lorem ipsum</span>
    </p>
  </div>

  <svg class="pie-chart" viewBox="0 0 1200 900" role="img" aria-label="Pie chart with six segments">
    <path d="M826 549 L826 317 A232 232 0 0 1 962.4 361.3 Z" fill="var(--slice-light-grey)"/>
    <path d="M826 549 L962.4 361.3 A232 232 0 0 1 1044 628.3 Z" fill="var(--slice-deep-blue)"/>
    <path d="M826 549 L1044 628.3 A232 232 0 0 1 909.1 765.7 Z" fill="var(--slice-mid-blue)"/>
    <path d="M826 549 L909.1 765.7 A232 232 0 0 1 607.3 626.5 Z" fill="var(--slice-pale-blue)"/>
    <path d="M826 549 L607.3 626.5 A232 232 0 0 1 695.2 357.4 Z" fill="var(--slice-dark-grey)"/>
    <path d="M826 549 L695.2 357.4 A232 232 0 0 1 826 317 Z" fill="var(--slice-grey)"/>
    <circle cx="826" cy="549" r="40" fill="var(--white)"/>

    <text class="slice-label label-dark" x="871" y="386"><tspan x="871">Lorem</tspan><tspan x="871" dy="25">ipsum</tspan><tspan x="871" dy="25">dolor</tspan></text>
    <text class="slice-label label-light" x="782" y="386"><tspan x="782">Lorem</tspan><tspan x="782" dy="25">ipsum</tspan><tspan x="782" dy="25">dolor</tspan></text>
    <text class="slice-label label-dark" x="954" y="512"><tspan x="954">Lorem ipsum</tspan><tspan x="954" dy="24">dolor</tspan></text>
    <text class="slice-label label-dark" x="934" y="644"><tspan x="934">Lorem ipsum</tspan><tspan x="934" dy="24">dolor</tspan></text>
    <text class="slice-label label-dark" x="762" y="658"><tspan x="762">Lorem ipsum dolor</tspan><tspan x="762" dy="24">Lorem ipsum dolor</tspan></text>
    <text class="slice-label label-light" x="697" y="511"><tspan x="697">Lorem ipsum dolor</tspan><tspan x="697" dy="24">Lorem ipsum dolor</tspan></text>
  </svg>

  <footer class="footer-band">
    <span class="copyright">Copyrighte@2014</span>
  </footer>
</body>
</html>
```